GHollis Busisness Card

I am an aerospace consultant and at this time only need business cards.

Industry/Entity Type

Business

Contact Information for Business Card

Hollis Partners,LLC
Gerald T. Hollis

348 Birch Hollow Road
Madison AL 35762

256-555-0148 (cell)
256-555-0173 (fax)

geraldhollis@mailbrook.net

```html
<!DOCTYPE html>
<html lang="en">
<head>
<meta charset="utf-8">
<title>Hollis Partners, LLC — Business Card</title>
<link rel="stylesheet" href="https://fonts.googleapis.com/css2?family=Open+Sans:wght@700&family=Arimo:wght@400&display=swap">
<style>
  :root {
    --page-bg: #dfe6f2;
    --card-navy-deep: #0b0a55;
    --card-navy: #16198a;
    --accent-blue: #5cc6f2;
    --text-white: #ffffff;
    --line-white: rgba(255, 255, 255, 0.75);
    --chart-glow: #2a34a8;
    --chart-green: #6fd35a;
  }
  * { box-sizing: border-box; margin: 0; padding: 0; }
  html, body {
    width: 1200px;
    height: 1000px;
    overflow: hidden;
    background: var(--page-bg);
  }
  .canvas {
    position: relative;
    width: 1200px;
    height: 1000px;
    display: flex;
    align-items: center;
    justify-content: center;
  }
  .business-card {
    position: relative;
    width: 1050px;
    height: 600px;
    overflow: hidden;
    background: linear-gradient(120deg, var(--card-navy-deep) 0%, var(--card-navy-deep) 40%, var(--card-navy) 100%);
    box-shadow: 0 10px 30px rgba(20, 30, 80, 0.25);
  }
  .chart-art {
    position: absolute;
    right: 0;
    top: 0;
    width: 640px;
    height: 600px;
  }
  .company-name {
    position: absolute;
    left: 48px;
    top: 40px;
    font-family: "Open Sans", sans-serif;
    font-weight: 700;
    font-size: 34px;
    letter-spacing: 1.5px;
    color: var(--text-white);
    text-transform: uppercase;
    padding-bottom: 8px;
    border-bottom: 4px solid var(--accent-blue);
  }
  .person-name {
    position: absolute;
    left: 40px;
    top: 128px;
    padding: 8px 14px;
    font-family: "Open Sans", sans-serif;
    font-weight: 700;
    font-size: 50px;
    letter-spacing: 2px;
    color: var(--text-white);
    text-transform: uppercase;
  }
  .person-name .bracket {
    position: absolute;
    width: 16px;
    height: 16px;
    border-color: var(--line-white);
    border-style: solid;
  }
  .bracket-tl { left: 0; top: 0; border-width: 3px 0 0 3px; }
  .bracket-br { right: 0; bottom: 0; border-width: 0 3px 3px 0; }
  .contact-block {
    position: absolute;
    left: 60px;
    top: 250px;
    font-family: "Arimo", sans-serif;
    font-size: 29px;
    line-height: 38px;
    color: var(--text-white);
  }
  .contact-block .address { margin-top: 22px; }
</style>
</head>
<body>
  <main class="canvas">
    <section class="business-card">
      <svg class="chart-art" viewBox="0 0 640 600" role="img" aria-label="Orbital star chart illustration with arcs, star points and green glowing planets">
        <defs>
          <radialGradient id="chartGlow" cx="65%" cy="60%" r="70%">
            <stop offset="0%" stop-color="#2b36ad"/>
            <stop offset="100%" stop-color="#141784"/>
          </radialGradient>
        </defs>
        <path d="M120 600 C 170 360, 330 170, 640 90 L 640 600 Z" fill="url(#chartGlow)"/>
        <path d="M120 600 C 170 360, 330 170, 640 90" fill="none" stroke="rgba(255,255,255,0.6)" stroke-width="3"/>
      </svg>

      <h2 class="company-name">Hollis Partners,LLC</h2>

      <h1 class="person-name">
        <span class="bracket bracket-tl"></span>
        Gerald T. Hollis
        <span class="bracket bracket-br"></span>
      </h1>

      <address class="contact-block" style="font-style: normal;">
        <p class="phone">M: 256-555-0148</p>
        <p class="fax">F: 256-555-0173</p>
        <p class="email">geraldhollis@mailbrook.net</p>
        <p class="address">348 Birch Hollow Road<br>Madison, AL 35762</p>
      </address>
    </section>
  </main>
</body>
</html>
```